A6 Advertising Post Card

I am looking for refinement on this idea for an advertising letter-box drop of an A6 postcard.
Side 1 - our brand, the address, "15% discount if you present this card before Dec 31"

We are a new retail concept in terms of the store concept.

Side 2 - i want to highlight where the products are from, what materials are used, emphasis on cool, fresh, different, affordable, the product ranges grouped by colours (storage &organisation items in 1 colour or font, illumination products in 1 colour or font, furniture in 1 colour or font, decor in 1 colour or font, curios is 1 colour or font, fasion in 1 colour or font, others in a 1 colour or font)

The Product Categories:
see attachment

Hi

I've added the product categories with products sorted under each heading. I have also added the logo in a variety of file types (jpg, tif, psd, png). The sky blue background is part of the brand image.
Thanks

Target Market(s)

Home-makers (men and women) and women of all ages. Decision makers for home furnishings. Cross demographic - this is not premium..affordable to all social strata.
The brand is about fun, colourful and functional home stuff. The fashion stuff is a small percentage of the overall offer - targeting women who should spoil themselves as they spoil their families with nice stuff for the home.

Industry/Entity Type

Advertising

```html
<!DOCTYPE html>
<html lang="en">
<head>
<meta charset="utf-8">
<title>Kalapa – A new store concept postcard</title>
<link rel="stylesheet" href="https://fonts.googleapis.com/css2?family=PT+Sans+Narrow:wght@400;700&display=swap">
<style>
  :root {
    --page: #e6e6e6;
    --sky: #6cc5cd;
    --navy: #3a3d62;
    --navy-deep: #1f2a52;
    --ink: #2c3766;
    --white: #ffffff;
    --illumination: #9b98b5;
    --storage: #f08a5a;
    --curios: #8ed0da;
    --furniture: #4461a9;
    --decor: #f0e615;
    --misc: #7b8b58;
    --fashion: #3c6a2c;
    --brand-dot: #c8322c;
    --wave-line: #5b6090;
  }
  * { margin: 0; padding: 0; box-sizing: border-box; }
  html, body { width: 1200px; height: 1000px; overflow: hidden; background: var(--page); }
  body { position: relative; font-family: "PT Sans Narrow", "Arial Narrow", sans-serif; }

  .card {
    position: absolute; left: 40px; top: 103px;
    width: 700px; height: 496px;
    transform: scale(1.6); transform-origin: 0 0;
    overflow: hidden; background: var(--navy);
  }
  .card-art { position: absolute; inset: 0; width: 700px; height: 496px; }

  .headline { position: absolute; left: 49px; top: 32px; color: var(--white); font-weight: 700; font-size: 25px; line-height: 1; }
  .values { position: absolute; left: 49px; top: 65px; color: var(--white); font-size: 14px; word-spacing: 1px; }
  .values .sep { margin: 0 4px; }

  .brand { position: absolute; left: 560px; top: 44px; display: flex; align-items: center; gap: 7px; }
  .brand-dot { width: 14px; height: 14px; border-radius: 50%; background: var(--brand-dot); }
  .brand-name { color: var(--ink); font-weight: 700; font-size: 30px; line-height: 1; }

  .origins {
    position: absolute; left: 49px; top: 137px; color: var(--ink);
    font-style: italic; font-size: 14.5px; line-height: 1.1;
    transform: rotate(1deg); transform-origin: 0 50%;
    white-space: nowrap;
  }
  .origins .sep { margin: 0 4px; }

  .range-label {
    position: absolute; writing-mode: vertical-rl; transform: rotate(180deg);
    font-weight: 700; font-size: 14px; line-height: 1; white-space: nowrap;
  }
  .range-list {
    position: absolute; list-style: none; color: var(--white);
    font-size: 10.4px; letter-spacing: -0.15px; line-height: 14px; white-space: nowrap;
  }
</style>
</head>
<body>
<div class="card">
  <svg class="card-art" viewBox="0 0 700 496">
    <defs>
      <linearGradient id="ph1" x1="0" x2="1"><stop offset="0" stop-color="#7e8a5c"/><stop offset="1" stop-color="#9a5a4c"/></linearGradient>
      <linearGradient id="ph2" x1="0" x2="1"><stop offset="0" stop-color="#ecebea"/><stop offset=".5" stop-color="#b27a7e"/><stop offset="1" stop-color="#ecebea"/></linearGradient>
      <linearGradient id="ph3" x1="0" x2="1"><stop offset="0" stop-color="#3c3a3e"/><stop offset=".5" stop-color="#a8745e"/><stop offset="1" stop-color="#3c3a3e"/></linearGradient>
      <linearGradient id="ph4" x1="0" x2="1"><stop offset="0" stop-color="#e6e4ea"/><stop offset=".6" stop-color="#c8d6dc"/><stop offset="1" stop-color="#e2c8cc"/></linearGradient>
      <linearGradient id="ph5" x1="0" x2="1"><stop offset="0" stop-color="#c89a68"/><stop offset=".6" stop-color="#a0563c"/><stop offset="1" stop-color="#8a8a8a"/></linearGradient>
    </defs>
    <rect class="header-band" x="0" y="0" width="700" height="300" fill="var(--sky)"/>
    <g class="photo-strip">
      <polygon points="0,176 125,168 125,278 0,280" fill="url(#ph1)" role="img" aria-label="Photo of colourful handmade beaded ornaments"/>
      <polygon points="130,168 272,172 272,284 130,277" fill="url(#ph2)" role="img" aria-label="Photo of a pink polka-dot gift bag"/>
      <polygon points="277,173 416,175 416,286 277,284" fill="url(#ph3)" role="img" aria-label="Photo of a woven natural-fibre planter with grass"/>
      <polygon points="420,175 555,168 555,278 420,286" fill="url(#ph4)" role="img" aria-label="Photo of striped cushions"/>
      <polygon points="560,167 700,154 700,262 560,277" fill="url(#ph5)" role="img" aria-label="Photo of wicker baskets and bowls"/>
    </g>
    <path class="wave-line" d="M0,172 C230,160 480,188 700,150" fill="none" stroke="var(--navy)" stroke-width="3"/>
    <path class="wave-line" d="M0,167 C230,155 480,183 700,145" fill="none" stroke="var(--navy)" stroke-width="1"/>
    <path class="lower-band" d="M0,280 C200,268 450,300 700,262 L700,496 L0,496 Z" fill="var(--navy)"/>
    <path d="M0,278 C200,266 450,298 700,260" fill="none" stroke="var(--white)" stroke-width="1" opacity=".7"/>
    <path class="footer-band" d="M0,470 C200,458 450,486 700,452 L700,496 L0,496 Z" fill="var(--navy-deep)"/>
    <path d="M0,462 C200,450 450,478 700,444" fill="none" stroke="var(--wave-line)" stroke-width="1"/>
    <path d="M0,466 C200,454 450,482 700,448" fill="none" stroke="var(--wave-line)" stroke-width="1"/>
    <g class="range-panels">
      <polygon points="49,282 138,278 138,496 49,496" fill="var(--illumination)"/>
      <polygon points="155,276 244,278 244,496 155,496" fill="var(--storage)"/>
      <polygon points="261,280 351,283 351,496 261,496" fill="var(--curios)"/>
      <polygon points="368,286 458,287 458,496 368,496" fill="var(--furniture)"/>
      <polygon points="474,283 564,276 564,496 474,496" fill="var(--decor)"/>
      <polygon points="581,268 670,265 670,385 581,385" fill="var(--misc)"/>
      <rect x="581" y="408" width="89" height="88" fill="var(--fashion)"/>
    </g>
  </svg>

  <h1 class="headline">A new store concept</h1>
  <p class="values">Fresh<span class="sep">•</span>Cool<span class="sep">•</span>Exotic<span class="sep">•</span>Modern</p>

  <div class="brand"><span class="brand-dot"></span><span class="brand-name">Kalapa</span></div>

  <p class="origins">Handmade&nbsp; from&nbsp; India<span class="sep">•</span>Philippines<span class="sep">•</span>Thailand<span class="sep">•</span>Indonesia<span class="sep">•</span>Malaysia<span class="sep">•</span>Nepal</p>

  <h2 class="range-label" style="left:36px; top:296px; color:var(--illumination);">Illumination</h2>
  <ul class="range-list" style="left:56px; top:311px;">
    <li>Glass Votives</li><li>Lamps</li><li>Moroccan Lanterns</li><li>Chandeliers</li><li>Candle Holders</li><li>Candles</li><li>Tee-light Holders</li><li>Pendant Lights</li><li>Lantern Stands</li>
  </ul>

  <h2 class="range-label" style="left:142px; top:300px; color:var(--storage);">Storage &amp; Organisation</h2>
  <ul class="range-list" style="left:161px; top:311px;">
    <li>Baskets</li><li>Trays</li><li>Drawers</li><li>Boxes</li><li>Tiffin Carrier</li><li>Plates</li><li>Bowls</li><li>Napkin Rings</li><li>Bamboo Towel Stands</li><li>Mugs</li><li>Cups</li><li>Jugs</li>
  </ul>

  <h2 class="range-label" style="left:249px; top:302px; color:var(--curios);">Curios</h2>
  <ul class="range-list" style="left:269px; top:311px;">
    <li>Figurines</li><li>Brass Statues</li><li>Telescopes</li><li>Compasses</li><li>Gramophone</li><li>Hour Glasses</li><li>Sextants</li><li>Magnifying Lens</li><li>Prayer Wheels</li><li>Singing Bowls</li><li>Incense Holder</li><li>Trumpet</li>
  </ul>

  <h2 class="range-label" style="left:356px; top:302px; color:var(--furniture);">Furniture</h2>
  <ul class="range-list" style="left:375px; top:311px;">
    <li>Cupboards</li><li>Tables</li><li>Stools</li><li>Chairs</li><li>Bookcases</li><li>Consoles</li><li>Cart</li><li>Trolley</li><li>Ceramic Knobs</li><li>Ladders</li><li>Umbrellas</li><li>Planters</li>
  </ul>

  <h2 class="range-label" style="left:462px; top:300px; color:var(--decor);">Decor</h2>
  <ul class="range-list" style="left:480px; top:311px;">
    <li>Cushions</li><li>Photo-frames</li><li>Decorative Ornaments</li><li>Vases</li><li>Bowls</li><li>Clocks</li><li>Mirrors</li><li>Bird Cages</li><li>Sedge Mats</li><li>Glass Decanters</li><li>Pattachitra Bottles</li><li>Bird Cage Stands</li>
  </ul>

  <h2 class="range-label" style="left:569px; top:302px; color:var(--misc);">Miscellaneous</h2>
  <ul class="range-list" style="left:588px; top:311px;">
    <li>Gift Bags</li><li>Wrapping Paper</li><li>Wine Bottle Holder</li><li>Xmas Decorations</li>
  </ul>

  <h2 class="range-label" style="left:569px; top:422px; color:var(--fashion);">Fashion</h2>
  <ul class="range-list" style="left:588px; top:423px;">
    <li>Shawls / Scarves</li><li>Bags</li><li>Bangles</li><li>Flip-Flops</li>
  </ul>
</div>
</body>
</html>
```